Three Banner Ad Concepts Multiple Sizes For Murmuro Native Ads Network Campaigns

I would like to see THREE totally different concepts using the content below. Once I approve the THREE DESIGN CONCEPTS I will need them in 5 different sizes for each of the 3 approved concepts.

So technically I am asking for THREE totally different designs in FIVE Sizes. See Sizes below.

I will advertise these banners on vorpla ad display network, tenvixads.example as well as murmuro so please keep these in mind and if you have experience creating these type of ads then this is great.

Headlines:
1. Boost Responses To Your Ads Without Increasing Ad Spend Giving Away Free Smartwatches and Sonettes You Don't Personally Need To Fulfill!

2. Attract More Customers During Tough Times Giving Away Free Vacation & Dining Vouchers That You Don't Need To Pay For!

3. Increase Conversions On Your Website Offering A Free Hotel Stay Or Even A Smart Watch In Exchange For Their Form Submission!

Calls To Actions:
1. Get A Free Sample Package
2. Sign Up For A Free Trial
3. Book A Demo

Native Ads Sizes
Image Size 600x600
Image Size 600x500
Image Size 600x315

Murmuro (for mm ads please take into account the 20% text rule in the image):
For carousel: 1200x1200 pixels
For regular image ads: 1200x628 pixels

Target Market(s)

B2B, Small Business Owners, Entrepreneurs, Marketing Directors, Sales Managers

Industry/Entity Type

Marketing

Requirements
Must have
• Use images from quarrypix.example as I have account here
Nice to have
• These designs need to be B2B based....Use images that compliment the TEXT and speak to a BUSINESS OWNER and NOT A CONSUMER!!
Should not have
• DO NOT CREATE AN AD THAT IS B2C based, this is a B2B ad. please check website www.bluefernrewardgroup.example

```html
<!DOCTYPE html>
<html lang="en">
<head>
<meta charset="utf-8">
<title>Bluefern Reward Group – Banner Concepts</title>
<link href="https://fonts.googleapis.com/css2?family=Open+Sans:wght@400;700;800&family=Oswald:wght@500;600&display=swap" rel="stylesheet">
<style>
  :root {
    --brand-blue: #1a6fc0;
    --deep-blue: #1e5d96;
    --ink: #1b1b1b;
    --grey-text: #555a60;
    --cta-yellow: #ffea00;
    --white: #ffffff;
    --rule-grey: #c9ccd0;
  }
  * { box-sizing: border-box; margin: 0; padding: 0; }
  html, body { width: 1200px; height: 400px; overflow: hidden; background: var(--white); }
  .canvas { position: relative; width: 1200px; height: 400px; display: flex; }
  .banner { position: relative; width: 400px; height: 400px; overflow: hidden; }

  .brand-name {
    font-family: "Open Sans", sans-serif;
    font-weight: 800;
    color: var(--brand-blue);
    text-align: center;
    line-height: 1.05;
    letter-spacing: 0.5px;
  }

  .cta {
    position: absolute;
    display: flex; align-items: center; justify-content: center;
    font-family: "Oswald", sans-serif;
    font-weight: 500;
    text-transform: uppercase;
    border-radius: 7px;
  }
  .cta--yellow { background: var(--cta-yellow); color: var(--ink); box-shadow: 0 2px 5px rgba(0,0,0,.25); }
  .cta--blue { background: var(--brand-blue); color: var(--white); }

  /* Concept 1 */
  .boost .photo {
    position: absolute; left: 180px; top: 0; width: 220px; height: 400px;
    background: linear-gradient(160deg, #f2f2f0 0%, #d9dcde 45%, #9aa5b2 75%, #6c7886 100%);
  }
  .boost .brand-name { position: absolute; left: 20px; top: 22px; width: 160px; font-size: 19px; }
  .boost .panel { position: absolute; left: 0; top: 97px; width: 210px; height: 303px; }
  .boost .panel svg { position: absolute; inset: 0; }
  .boost .headline {
    position: absolute; left: 0; top: 14px; width: 180px;
    font-family: "Open Sans", sans-serif; font-weight: 700;
    color: var(--white); font-size: 22px; line-height: 1.2; text-align: center; text-transform: uppercase;
  }
  .boost .body {
    position: absolute; left: 8px; top: 106px; width: 164px;
    font-family: "Open Sans", sans-serif; color: var(--white);
    font-size: 12.5px; line-height: 1.38; text-align: center; text-transform: uppercase;
  }
  .boost .divider { position: absolute; left: 12px; width: 156px; height: 1px; background: rgba(255,255,255,.35); }
  .boost .cta { left: 20px; top: 347px; width: 139px; height: 35px; font-size: 19px; }

  /* Concept 2 */
  .attract .photo {
    position: absolute; inset: 0;
    background: linear-gradient(90deg, #ffffff 0%, #ffffff 22%, rgba(255,255,255,.6) 42%, rgba(255,255,255,0) 62%),
                linear-gradient(180deg, #4e6a86 0%, #c9b6a3 40%, #d6dde6 70%, #2f3f58 100%);
  }
  .attract .brand-name { position: absolute; left: 40px; top: 30px; width: 115px; font-size: 19px; }
  .attract .copy {
    position: absolute; left: 5px; top: 123px; width: 290px;
    font-family: "Open Sans", sans-serif; text-align: center;
  }
  .attract .accent { color: var(--brand-blue); font-weight: 800; font-size: 22px; line-height: 1.0; }
  .attract .plain { color: var(--grey-text); font-size: 19.5px; line-height: 1.1; margin: 3px 0; }
  .attract .cta { left: 38px; top: 315px; width: 107px; height: 25px; font-size: 14px; }

  /* Concept 3 */
  .convert .people {
    position: absolute; left: 0; top: 185px; width: 400px; height: 215px;
    background: linear-gradient(180deg, #f4f4f4 0%, #8a8d92 35%, #2a2c30 70%, #151618 100%);
  }
  .convert .band { position: absolute; inset: 0 0 auto 0; height: 170px; }
  .convert .headline {
    position: absolute; left: 0; top: 8px; width: 400px; text-align: center;
    font-family: "Oswald", sans-serif; font-weight: 500; color: var(--white);
    font-size: 37px; line-height: 1.02; text-transform: uppercase; transform: scaleX(.9);
  }
  .convert .sub {
    position: absolute; left: 0; top: 95px; width: 400px; text-align: center;
    font-family: "Oswald", sans-serif; font-weight: 500; color: var(--white);
    font-size: 15px; line-height: 1.5; text-transform: uppercase; transform: scaleX(.85);
  }
  .convert .cta { left: 128px; top: 147px; width: 140px; height: 33px; font-size: 19px; }
  .convert .seal { position: absolute; left: 0; top: 290px; width: 160px; height: 110px; }
  .convert .brand-name { position: absolute; left: 12px; top: 330px; width: 120px; font-size: 17px; }
</style>
</head>
<body>
<main class="canvas">

  <section class="banner boost">
    <div class="photo" role="img" aria-label="Delighted businessman in a light blazer holding a tablet"></div>
    <div class="brand-name">BLUEFERN<br>REWARD GROUP</div>
    <div class="panel">
      <svg width="210" height="303" viewBox="0 0 210 303">
        <path d="M0 0 H200 C185 90 178 200 190 303 H0 Z" fill="var(--deep-blue)"/>
      </svg>
      <h2 class="headline">Boost Responses to Your Ads</h2>
      <div class="divider" style="top:96px"></div>
      <p class="body">Without increasing ad spend giving away free smartwatches and Sonettes you don't personally need to fulfill!</p>
      <div class="divider" style="top:296px"></div>
    </div>
    <span class="cta cta--yellow">Book a Demo</span>
  </section>

  <section class="banner attract">
    <div class="photo" role="img" aria-label="Smiling young man in a striped shirt working on a laptop in an office"></div>
    <div class="brand-name">BLUEFERN<br>REWARD GROUP</div>
    <div class="copy">
      <p class="accent">Attract More<br>Customers</p>
      <p class="plain">During Tough Times<br>Giving Away Free<br>Vacation &amp; Dining<br>Vouchers That</p>
      <p class="accent">You Don't Need<br>To Pay For!</p>
    </div>
    <span class="cta cta--blue">Book a Demo</span>
  </section>

  <section class="banner convert">
    <div class="people" role="img" aria-label="Confident business team in dark suits standing with arms crossed"></div>
    <svg class="band" width="400" height="170" viewBox="0 0 400 170">
      <path d="M0 0 H400 V140 C280 160 140 165 0 150 Z" fill="var(--rule-grey)"/>
      <path d="M0 0 H400 V135 C280 152 140 158 0 143 Z" fill="var(--brand-blue)"/>
    </svg>
    <h2 class="headline">Increase Conversions<br>on Your Website</h2>
    <p class="sub">Offering a free hotel stay or even a smart watch<br>in exchange for their form submission!</p>
    <span class="cta cta--yellow">Book a Demo</span>
    <svg class="seal" width="160" height="110" viewBox="0 0 160 110">
      <circle cx="75" cy="115" r="88" fill="var(--brand-blue)"/>
      <circle cx="72" cy="120" r="82" fill="var(--white)"/>
    </svg>
    <div class="brand-name">BLUEFERN<br>REWARD GROUP</div>
  </section>

</main>
</body>
</html>
```